Redesign of an existing webpage

We've just redesigned our logo on a new website design to reflect the new logo. That wants to change the color and graphical appearance of our website. There are no restrictions on what should be changed. IT should display our portfolio and pricing and explain our product. Please provide stock photos if needed. The site structure should not be changed. So we want the pages which are currently there. We need the following pages: Main page (Home page) Detail page (currently used at AGB and questions) Imprint (including the map) existing webpage: www.plorvane.de
Updates

I've got a request from one of the designers-

Target Market(s)

We are offering IT services to small companies. The do not need own IT equipment or PC Specialists if if our service.

Industry/Entity Type

It Service

Coding

Coded - Design and coding required

Number of Pages Required

3 page

Font styles to use
Other font styles liked:
• Relaway

Colors

Designer to choose colors to be used in the design.

Requirements
Must have
• our login mask at https://desktop.plorvane.com needs a rebranding too

```html
<!DOCTYPE html>
<html lang="de">
<head>
<meta charset="utf-8">
<title>Plorvane – Einfach arbeiten</title>
<link href="https://fonts.googleapis.com/css2?family=Raleway:ital,wght@0,400;0,500;0,600;0,700;0,800;1,400;1,600&display=swap" rel="stylesheet">
<style>
:root{
  --navy:#1d3c5e;
  --navy-deep:#17324f;
  --blue:#2b73c2;
  --sky:#bcdcf5;
  --gold:#f5b52c;
  --ink:#2b2b2b;
  --muted:#8a8a8a;
  --light:#f7f7f8;
  --line:#e6e6e6;
  --footer:#3b3b3d;
}
*{box-sizing:border-box;margin:0;padding:0}
html,body{width:1200px;height:4520px;overflow:hidden}
body{position:relative;font-family:'Raleway',sans-serif;color:var(--ink);background:#fff}
.abs{position:absolute}
.center{text-align:center}
.h2{position:absolute;left:0;width:1200px;text-align:center;font-size:21px;font-weight:700;letter-spacing:.3px;color:var(--ink)}
.lead{position:absolute;left:250px;width:700px;text-align:center;font-size:8.5px;font-style:italic;line-height:15px;color:var(--muted)}
.gold-dash{display:block;width:28px;height:2px;background:var(--gold);margin:4px 0}
/* nav */
.nav{position:absolute;left:0;top:0;width:1200px;height:60px;background:#fff}
.brand{position:absolute;left:256px;top:17px;font-size:21px;font-weight:800;color:var(--navy);letter-spacing:1px}
.menu{position:absolute;left:520px;top:23px;display:flex;gap:34px;font-size:11px;color:var(--ink)}
.menu .active{color:var(--blue)}
.nav-cta{position:absolute;left:850px;top:15px;width:94px;height:28px;border:1px solid var(--gold);border-radius:2px;color:var(--gold);font-size:11px;text-align:center;line-height:26px}
/* hero */
.hero{position:absolute;left:0;top:60px;width:1200px;height:540px;background:linear-gradient(135deg,#4b3f35 0%,#2a2622 40%,#39424e 70%,#1f2833 100%)}
.hero-title{position:absolute;left:0;top:170px;width:1200px;text-align:center;color:#fff;font-size:27px;font-weight:700;letter-spacing:1px}
.hero-bar{position:absolute;left:578px;top:210px;width:44px;height:3px;background:var(--gold)}
.hero-text{position:absolute;left:280px;top:232px;width:640px;text-align:center;color:#fff;font-size:13px;line-height:19px;font-weight:500}
.btn-ghost{position:absolute;top:333px;width:140px;height:38px;border:1px solid #fff;color:#fff;font-size:13px;text-align:center;line-height:36px;border-radius:2px}
/* intro */
.intro-photo{position:absolute;left:254px;top:733px;width:351px;height:456px;background:linear-gradient(160deg,#e9e6e1,#b9b3ab 55%,#6e6862);box-shadow:0 6px 18px rgba(0,0,0,.18)}
.feature{position:absolute;left:646px;width:300px}
.feature .ic{position:absolute;left:0;top:0}
.feature h4{margin-left:54px;font-size:12px;font-weight:500;color:var(--ink)}
.feature .gold-dash{margin-left:54px}
.feature p{margin-left:54px;font-size:8.5px;line-height:15px;color:var(--muted);text-align:justify}
/* benefits */
.benefits{position:absolute;left:0;top:1258px;width:1200px;height:794px;background:var(--light)}
.card{position:absolute;width:211px;height:131px;background:#fff;border:1px solid var(--line)}
.card .badge{position:absolute;left:30px;top:-16px;width:36px;height:36px;border-radius:50%;background:#fff;border:1px solid var(--line);display:flex;align-items:center;justify-content:center}
.card h4{position:absolute;left:22px;top:32px;font-size:12px;font-weight:500}
.card .gold-dash{position:absolute;left:22px;top:48px;margin:0}
.card p{position:absolute;left:22px;top:58px;width:168px;font-size:8.5px;line-height:14.5px;color:var(--muted);text-align:justify}
/* steps */
.step-line{position:absolute;left:321px;top:2243px;width:556px;height:1px;background:var(--line)}
.step{position:absolute;width:170px;text-align:center}
.step .dot{width:44px;height:44px;border-radius:50%;background:#fff;border:1px solid var(--line);margin:0 auto;display:flex;align-items:center;justify-content:center}
.step h4{margin-top:12px;font-size:12px;font-weight:500}
.step .gold-dash{margin:5px auto}
.step p{width:130px;margin:0 auto;font-size:8.5px;line-height:14.5px;color:var(--muted)}
/* pricing */
.price{position:absolute;top:2631px;width:251px;height:307px;background:#fff;box-shadow:0 4px 18px rgba(0,0,0,.1);overflow:hidden;text-align:center}
.price .corner{position:absolute;left:0;top:0}
.price .icon{margin-top:14px}
.price h5{font-size:11px;font-weight:500;margin-top:6px;letter-spacing:.5px}
.price .amount{font-size:24px;font-weight:700;color:var(--gold);margin-top:4px}
.price .per{font-size:9px;color:var(--ink);margin-top:4px}
.price .bar{width:44px;height:2px;background:var(--gold);margin:6px auto 0}
.price ul{list-style:none;margin:12px 32px 0;text-align:left}
.price li{display:flex;justify-content:space-between;font-size:8.5px;color:var(--muted);height:22px;align-items:center}
.price li.gap{margin-top:10px}
.price .cta{position:absolute;left:66px;bottom:24px;width:119px;height:26px;border:1px solid var(--gold);color:var(--gold);font-size:9px;line-height:24px;border-radius:2px}
/* testimonials */
.voices{position:absolute;left:0;top:3008px;width:1200px;height:491px;background:linear-gradient(180deg,#244769 0%,#1b3756 100%)}
.voice{position:absolute;top:3145px;width:212px;height:147px;background:#fff;text-align:center}
.voice p{margin:22px 20px 0;font-size:8.5px;line-height:14.5px;color:var(--muted)}
.voice .who{position:absolute;left:0;bottom:18px;width:100%;display:flex;justify-content:center;align-items:center;gap:10px;font-size:11px;color:var(--ink)}
.quote-mark{color:var(--gold);font-size:12px}
/* highlight */
.highlight{position:absolute;left:254px;top:3362px;width:690px;height:269px;background:#fff;box-shadow:0 4px 18px rgba(0,0,0,.12)}
.highlight .shot{position:absolute;left:0;top:0;width:307px;height:269px;background:linear-gradient(135deg,#e6e9ec,#9aa5ae 60%,#3f4953)}
.highlight h3{position:absolute;left:347px;top:55px;font-size:14px;font-weight:700}
.highlight .gold-dash{position:absolute;left:347px;top:74px;margin:0}
.highlight p{position:absolute;left:347px;top:90px;width:305px;font-size:8.5px;line-height:16px;color:var(--muted);text-align:justify}
/* founders */
.avatar{position:absolute;left:567px;top:3808px;width:66px;height:66px;border-radius:50%;background:linear-gradient(160deg,#c99a74,#7b5a45)}
.founder-name{position:absolute;left:0;top:3890px;width:1200px;text-align:center;font-size:12px;font-weight:500}
.founder-role{position:absolute;left:0;top:3908px;width:1200px;text-align:center;font-size:8px;font-style:italic;color:var(--muted)}
.founder-bio{position:absolute;left:380px;top:3944px;width:440px;text-align:center;font-size:9px;line-height:16px;color:var(--muted)}
.founder-quote{position:absolute;left:400px;top:4035px;width:400px;text-align:center;font-size:9px;line-height:16px;font-weight:600;font-style:italic}
/* social */
.social{position:absolute;top:4264px;width:130px;text-align:center}
.social .ring{width:56px;height:56px;border-radius:50%;border:2px solid var(--blue);margin:0 auto;display:flex;align-items:center;justify-content:center;color:var(--blue);font-size:18px;font-weight:700}
.social .handle{margin-top:18px;height:26px;border:1px solid var(--gold);color:var(--gold);font-size:9px;line-height:24px}
.footer{position:absolute;left:0;top:4457px;width:1200px;height:63px;background:var(--footer);color:#ddd;font-size:9px}
.footer .links{position:absolute;left:256px;top:27px;display:flex;gap:30px}
.footer .copy{position:absolute;right:256px;top:27px}
</style>
</head>
<body>

<header class="nav">
  <div class="brand">PLORVANE</div>
  <nav class="menu"><span class="active">Home</span><span>So geht's</span><span>Preise</span><span>Über Uns</span><span>Fragen</span></nav>
  <div class="nav-cta">Jetzt loslegen</div>
</header>

<section class="hero" role="img" aria-label="Foto: Hände an Laptops auf einem Holztisch, Arbeitsplatz im Team"></section>
<h1 class="hero-title">EINFACH ARBEITEN.</h1>
<div class="hero-bar"></div>
<p class="hero-text">In großen Unternehmen sorgen EDV-Abteilungen für eine funktionierende IT. Dabei kommen zentrale Server zum Einsatz, auf die von den einzelnen Arbeitsplätzen aus zugegriffen wird. Plorvane hat sich das Ziel gesetzt, auch kleinen und mittleren Unternehmen zu überschaubaren Kosten solch eine Lösung zur Verfügung zu stellen.</p>
<div class="btn-ghost" style="left:446px">Jetzt Loslegen</div>
<div class="btn-ghost" style="left:616px">Mehr Erfahren</div>
<svg class="abs" style="left:560px;top:560px" width="80" height="40" viewBox="0 0 80 40"><path d="M0 40 C20 40 22 8 40 8 C58 8 60 40 80 40Z" fill="#fff"/><path d="M40 18v14M34 26l6 6 6-6" stroke="#f5b52c" stroke-width="2" fill="none"/></svg>

<h2 class="h2" style="top:664px">IT, DIE EINFACH FUNKTIONIERT</h2>
<div class="intro-photo" role="img" aria-label="Foto: Frau arbeitet am Laptop"></div>

<div class="feature" style="top:733px">
  <svg class="ic" width="40" height="40" viewBox="0 0 40 40" fill="none" stroke="#2b73c2" stroke-width="1.5"><circle cx="20" cy="10" r="5"/><circle cx="8" cy="26" r="4"/><circle cx="32" cy="26" r="4"/><path d="M20 15v8M12 26h16"/><circle cx="20" cy="34" r="3" stroke="#f5b52c"/></svg>
  <h4>Das Problem</h4><span class="gold-dash"></span>
  <p>Die Basis der IT-Probleme, die Ihren Geschäftsalltag unnötig erschweren, ist – neben dem menschlichen Faktor – der Rechner selbst, denn dort landen Viren, werden Programme lahm und gehen Daten verloren.</p>
</div>
<div class="feature" style="top:843px">
  <svg class="ic" width="40" height="40" viewBox="0 0 40 40" fill="none" stroke="#2b73c2" stroke-width="1.5"><rect x="4" y="22" width="6" height="14"/><rect x="14" y="16" width="6" height="20"/><rect x="24" y="10" width="6" height="26"/><path d="M4 14l10-6 8 4 12-8" stroke="#f5b52c"/></svg>
  <h4>Unsere Lösung</h4><span class="gold-dash"></span>
  <p>Plorvane bietet Ihnen eine Lösung, mit der die tägliche Sicherung Ihrer Daten und die Überwachung der Funktionsbereitschaft Ihres Systems gewährleistet sind. Dazu setzen wir an der Basis an: alles, was Sie zum Arbeiten brauchen, wird auf die Server unseres Rechenzentrums verlagert. Alle notwendigen rechtlichen und sonstigen Anforderungen werden dort von uns umgesetzt.</p>
</div>
<div class="feature" style="top:1013px">
  <svg class="ic" width="40" height="40" viewBox="0 0 40 40" fill="none" stroke="#2b73c2" stroke-width="1.5"><path d="M20 4l13 5v10c0 9-6 14-13 17C13 33 7 28 7 19V9z"/><path d="M14 20l4 4 8-8" stroke="#f5b52c"/></svg>
  <h4>Ihre Sicherheit</h4><span class="gold-dash"></span>
  <p>Wenn Sie sich fragen, wie sicher unsere Lösung ist, dann ist die Antwort ganz einfach: sehr sicher. Wir arbeiten mit einem der größten Rechenzentren Deutschlands zusammen. Die Sicherheitsvorkehrungen dieses Rechenzentrums gleichen denen eines Hochsicherheitstrakts. Ihre Daten sind dort vor Schadsoftware, unerlaubtem Zugriff und sogar Naturkatastrophen geschützt und bei Stromausfall sorgen Generatoren und Reservebatterien für den fortlaufenden Betrieb.</p>
</div>

<section class="benefits"></section>
<h2 class="h2" style="top:1322px">IHR NUTZEN IM ÜBERBLICK</h2>
<p class="lead" style="top:1362px">Setzen Sie Ressourcen für Ihr Kerngeschäft frei, denn um zeitraubende Störungen wie lahme Programme, Virenbefall, Datenverlust etc. müssen Sie sich weder selbst kümmern, noch müssen Sie einen externen Dienstleister zur Behebung buchen. Kapazitäts- und Speicherprobleme gehören der Vergangenheit an und Ihr Betriebssystem wird durch das Rechenzentrum aktualisiert – schneller, direkter und deutlich sicherer, als das bei Ihnen vor Ort geschehen könnte. Nutzen Sie unsere Thin Clients, entfallen außerdem weitere Investitionen in Ihre EDV-Infrastruktur.</p>

<div class="card" style="left:258px;top:1491px"><div class="badge"><svg width="18" height="18" viewBox="0 0 18 18" fill="none" stroke="#2b73c2" stroke-width="1.3"><rect x="2" y="3" width="14" height="12"/><path d="M2 7h14M6 1v4M12 1v4"/></svg></div><h4>Expressentstörung</h4><span class="gold-dash"></span><p>Montags bis Freitags erfolgt die Störungsbehebung in maximal 8 Stunden durch den Plorvane Support.</p></div>
<div class="card" style="left:495px;top:1491px"><div class="badge"><svg width="18" height="18" viewBox="0 0 18 18" fill="none" stroke="#2b73c2" stroke-width="1.3"><rect x="2" y="4" width="14" height="10"/><circle cx="9" cy="9" r="2.5"/></svg></div><h4>Schnelle Programme</h4><span class="gold-dash"></span><p>Unsere Technologie holt die maximale Geschwindigkeit aus Ihren bestehenden Anwendungen heraus.</p></div>
<div class="card" style="left:731px;top:1491px"><div class="badge"><svg width="18" height="18" viewBox="0 0 18 18" fill="none" stroke="#2b73c2" stroke-width="1.3"><path d="M9 2l6 2.5v5c0 4-3 6-6 7-3-1-6-3-6-7v-5z"/></svg></div><h4>Professioneller Schutz</h4><span class="gold-dash"></span><p>In unserem Service ist ein professioneller Schutz vor Viren, Cryptoviren, Trojanern und anderen Schädlingen enthalten.</p></div>

<div class="card" style="left:258px;top:1672px"><div class="badge"><svg width="18" height="18" viewBox="0 0 18 18" fill="none" stroke="#2b73c2" stroke-width="1.3"><ellipse cx="9" cy="4" rx="6" ry="2"/><path d="M3 4v10c0 1 3 2 6 2s6-1 6-2V4M3 9c0 1 3 2 6 2s6-1 6-2"/></svg></div><h4>Datensicherung</h4><span class="gold-dash"></span><p>Tägliche Datensicherung und damit Schutz vor Datenverlust – von uns kontrolliert und jederzeit wiederherstellbar.</p></div>
<div class="card" style="left:495px;top:1672px"><div class="badge"><svg width="18" height="18" viewBox="0 0 18 18" fill="none" stroke="#2b73c2" stroke-width="1.3"><path d="M9 16V8M9 8c0-4 3-6 6-6 0 4-3 6-6 6zM9 10C9 7 7 5 3 5c0 3 2 5 6 5z"/></svg></div><h4>Nachhaltig</h4><span class="gold-dash"></span><p>Die eingesetzten Server-Systeme werden mit regenerativen Energien des Stromlieferanten Stromvia betrieben.</p></div>
<div class="card" style="left:731px;top:1672px"><div class="badge"><svg width="18" height="18" viewBox="0 0 18 18" fill="none" stroke="#2b73c2" stroke-width="1.3"><rect x="3" y="2" width="12" height="14"/><path d="M6 6h6M6 9h6M6 12h3"/></svg></div><h4>Planbare Kosten</h4><span class="gold-dash"></span><p>Unsere monatliche Kostenverteilung. Zusatzkosten durch Defekte, Erweiterungen oder teure vor Ort Einsätze fallen nicht an.</p></div>

<div class="card" style="left:258px;top:1854px"><div class="badge"><svg width="18" height="18" viewBox="0 0 18 18" fill="none" stroke="#2b73c2" stroke-width="1.3"><rect x="2" y="3" width="14" height="10"/><path d="M6 16h6M9 13v3M6 9l2-2 2 2 3-3"/></svg></div><h4>Updates</h4><span class="gold-dash"></span><p>Zentrale Aktualisierung Ihres Betriebssystems mit Funktionsupdates und Sicherheitsupdates.</p></div>
<div class="card" style="left:495px;top:1854px"><div class="badge"><svg width="18" height="18" viewBox="0 0 18 18" fill="none" stroke="#2b73c2" stroke-width="1.3"><rect x="4" y="8" width="10" height="8"/><path d="M6 8V5a3 3 0 016 0v3"/></svg></div><h4>Hohe Sicherheit</h4><span class="gold-dash"></span><p>Zentrale EDV-Leistungen aus hochsicheren Rechenzentren.</p></div>
<div class="card" style="left:731px;top:1854px"><div class="badge"><svg width="18" height="18" viewBox="0 0 18 18" fill="none" stroke="#2b73c2" stroke-width="1.3"><rect x="2" y="3" width="14" height="10"/><path d="M6 16h6M9 13v3"/></svg></div><h4>Gewohnte Software</h4><span class="gold-dash"></span><p>Die Benutzeroberfläche sieht so aus, wie Sie es gewohnt sind.</p></div>

<h2 class="h2" style="top:2117px">WIE WERDE ICH KUNDE?</h2>
<p class="lead" style="top:2156px">Um Kunde bei Plorvane zu werden sind die nachfolgenden vier Schritte erforderlich</p>
<div class="step-line"></div>
<div class="step" style="left:236px;top:2221px"><div class="dot"><svg width="20" height="20" viewBox="0 0 20 20" fill="none" stroke="#2b73c2" stroke-width="1.3"><path d="M4 3v14M10 3v14M16 3v14"/><circle cx="4" cy="7" r="2"/><circle cx="10" cy="13" r="2"/><circle cx="16" cy="8" r="2"/></svg></div><h4>Service auswählen</h4><span class="gold-dash"></span><p>Plorvane bietet zwei verschiedene Modelle an. Entscheiden Sie sich für eines dieser Modelle.</p></div>
<div class="step" style="left:422px;top:2221px"><div class="dot"><svg width="20" height="20" viewBox="0 0 20 20" fill="none" stroke="#2b73c2" stroke-width="1.3"><rect x="3" y="4" width="14" height="11"/><path d="M3 5l7 5 7-5"/></svg></div><h4>Anfrage absenden</h4><span class="gold-dash"></span><p>Füllen Sie unverbindlich unser Formular zur Vertragsanfrage aus. Wir bewerten die Machbarkeit und erstellen einen Vertragsentwurf.</p></div>
<div class="step" style="left:608px;top:2221px"><div class="dot"><svg width="20" height="20" viewBox="0 0 20 20" fill="none" stroke="#2b73c2" stroke-width="1.3"><rect x="4" y="2" width="12" height="16"/><path d="M7 6h6M7 9h6M7 12h4"/></svg></div><h4>Vertrag unterschreiben</h4><span class="gold-dash"></span><p>Den unterschriebenen Vertrag können Sie uns auf dem Postweg oder per E-Mail zukommen lassen.</p></div>
<div class="step" style="left:792px;top:2221px"><div class="dot"><svg width="20" height="20" viewBox="0 0 20 20" fill="none" stroke="#2b73c2" stroke-width="1.3"><circle cx="10" cy="10" r="6"/><path d="M10 2v3M10 15v3M2 10h3M15 10h3"/></svg></div><h4>Losarbeiten</h4><span class="gold-dash"></span><p>Sobald der Vertrag eingegangen ist, können Sie innerhalb von fünf Werktagen losarbeiten.</p></div>

<h2 class="h2" style="top:2520px">SERVICE AUSWÄHLEN</h2>
<p class="lead" style="top:2558px">Wählen Sie Ihren Service: Plorvane stellt im Modell Thin Client einen vollständigen Arbeitsplatz bereit. Es wird lediglich ein Monitor benötigt um loszuarbeiten. Beide Services sind mit einem bestehenden PC, Laptop oder Tablet von jedem Ort aus verschlüsselt nutzbar.</p>

<div class="price" style="left:328px">
  <svg class="corner" width="90" height="44"><path d="M0 0h90L0 44z" fill="#bcdcf5"/></svg>
  <svg class="icon" width="40" height="36" viewBox="0 0 40 36" fill="none" stroke="#2b73c2" stroke-width="1.5"><rect x="14" y="2" width="22" height="16"/><path d="M20 24h10M25 18v6"/><circle cx="9" cy="14" r="4"/><path d="M2 34c0-7 3-11 7-11s7 4 7 11"/></svg>
  <h5>THIN CLIENT</h5><div class="amount">99 €</div><div class="per">pro Benutzer/Monat (ab 5 Benutzer)</div><div class="bar"></div>
  <ul>
    <li>bis 5 Benutzer 115 € / Monat <svg width="12" height="10"><path d="M1 5l3 3 7-7" stroke="#2b73c2" stroke-width="1.5" fill="none"/></svg></li>
    <li>bis 5 Benutzer 115 € / Monat <svg width="12" height="10"><path d="M1 5l3 3 7-7" stroke="#2b73c2" stroke-width="1.5" fill="none"/></svg></li>
    <li class="gap">bis 5 Benutzer 115 € / Monat <svg width="12" height="10"><path d="M1 5l3 3 7-7" stroke="#2b73c2" stroke-width="1.5" fill="none"/></svg></li>
    <li>bis 5 Benutzer 115 € / Monat <svg width="12" height="10"><path d="M1 5l3 3 7-7" stroke="#2b73c2" stroke-width="1.5" fill="none"/></svg></li>
  </ul>
  <div class="cta">Jetzt loslegen</div>
</div>
<div class="price" style="left:621px">
  <svg class="corner" width="90" height="44"><path d="M0 0h90L0 44z" fill="#bcdcf5"/></svg>
  <svg class="icon" width="40" height="36" viewBox="0 0 40 36" fill="none" stroke="#2b73c2" stroke-width="1.5"><rect x="6" y="2" width="28" height="20"/><rect x="11" y="7" width="18" height="10"/><path d="M14 30h12M20 22v8"/></svg>
  <h5>BRING YOUR OWN</h5><div class="amount">75 €</div><div class="per">pro Benutzer/Monat (ab 5 Benutzer)</div><div class="bar"></div>
  <ul>
    <li>bis 5 Benutzer 115 € / Monat <svg width="12" height="10"><path d="M1 5l3 3 7-7" stroke="#2b73c2" stroke-width="1.5" fill="none"/></svg></li>
    <li>bis 5 Benutzer 115 € / Monat <svg width="12" height="10"><path d="M1 5l3 3 7-7" stroke="#2b73c2" stroke-width="1.5" fill="none"/></svg></li>
    <li class="gap">bis 5 Benutzer 115 € / Monat <svg width="12" height="10"><path d="M1 5l3 3 7-7" stroke="#2b73c2" stroke-width="1.5" fill="none"/></svg></li>
    <li>bis 5 Benutzer 115 € / Monat <svg width="12" height="10"><path d="M1 5l3 3 7-7" stroke="#2b73c2" stroke-width="1.5" fill="none"/></svg></li>
  </ul>
  <div class="cta">Jetzt loslegen</div>
</div>

<section class="voices" role="img" aria-label="Foto: Team im Büro, dunkelblau eingefärbt"></section>
<h2 class="h2" style="top:3072px;color:#fff">WAS UNSERE KUNDEN SAGEN</h2>
<div class="voice" style="left:137px"><p><span class="quote-mark">“</span> Ich bin überall arbeitsfähig. Konkurrenten mussten nach einem Cryptovirus Insolvenz anmelden. Meine Daten sind sicher <span class="quote-mark">„</span></p><div class="who"><svg width="30" height="26" viewBox="0 0 30 26" fill="none" stroke="#2b73c2" stroke-width="1.4"><path d="M3 12L15 3l12 9M6 10v14h18V10"/><rect x="12" y="16" width="6" height="8"/></svg>Hausverwalter</div></div>
<div class="voice" style="left:374px"><p><span class="quote-mark">“</span> Ich bin überall arbeitsfähig. Konkurrenten mussten nach einem Cryptovirus Insolvenz anmelden. Meine Daten sind sicher <span class="quote-mark">„</span></p><div class="who"><svg width="30" height="26" viewBox="0 0 30 26" fill="none" stroke="#2b73c2" stroke-width="1.4"><circle cx="15" cy="9" r="5"/><path d="M5 25c0-7 4-10 10-10s10 3 10 10M9 6h12"/></svg>Elektriker</div></div>
<div class="voice" style="left:610px"><p><span class="quote-mark">“</span> Ich bin überall arbeitsfähig. Konkurrenten mussten nach einem Cryptovirus Insolvenz anmelden. Meine Daten sind sicher <span class="quote-mark">„</span></p><div class="who"><svg width="30" height="26" viewBox="0 0 30 26" fill="none" stroke="#2b73c2" stroke-width="1.4"><circle cx="11" cy="8" r="5"/><path d="M2 25c0-7 4-10 9-10M18 16l3 3 6-6"/></svg>Qualitätsberater</div></div>
<div class="voice" style="left:849px"><p><span class="quote-mark">“</span> Ich bin überall arbeitsfähig. Konkurrenten mussten nach einem Cryptovirus Insolvenz anmelden. Meine Daten sind sicher <span class="quote-mark">„</span></p><div class="who"><svg width="30" height="26" viewBox="0 0 30 26" fill="none" stroke="#2b73c2" stroke-width="1.4"><rect x="3" y="8" width="24" height="16"/><path d="M3 8l3-6h18l3 6M9 14h4v6H9zM17 14h5v4h-5z"/></svg>Einzelhändler</div></div>

<div class="highlight">
  <div class="shot" role="img" aria-label="Foto: Laptop mit Programmcode auf dem Bildschirm neben einer Pflanze"></div>
  <h3>EINFACH, ZUVERLÄSSIG UND GÜNSTIG</h3><span class="gold-dash"></span>
  <p>Große Unternehmen arbeiten schon seit Jahren so und konnten damit ihre Kosten senken und die Stabilität erhöhen. Jetzt bietet Plorvane die Lösung auch für kleinere Unternehmen an. Wir speichern Ihre Daten dauerhaft an einem sicheren Ort. Notwendige Sicherheitsvorkehrungen werden getroffen. Ihre Daten werden gesichert und Sie konzentrieren sich auf Ihr tägliches Geschäft.</p>
  <svg class="abs" style="right:0;bottom:0" width="22" height="22"><path d="M22 0v22H0z" fill="#6fa8dc"/></svg>
</div>

<h2 class="h2" style="top:3698px">DIE GRÜNDER</h2>
<p class="lead" style="top:3738px">Die Firma Plorvane wurde am 18.03.2019 von Lukas Brennholt und Jonas Veltrup gegründet. Der Gründung ging eine zweijährige Test- und Projektierungs-Phase voraus. Der Hauptsitz der Firma befindet sich am beschaulichen Mühlenweg.</p>
<div class="avatar" role="img" aria-label="Porträtfoto des Gründers"></div>
<div class="founder-name">Jonas Veltrup</div>
<div class="founder-role">Gründer und Geschäftsführer</div>
<p class="founder-bio">Jonas ist 46 Jahre alt, verheiratet und hat zwei Kinder. Er ist seit mittlerweile 19 Jahren in der IT tätig und ist als gelernter Kaufmann quer eingestiegen. Neben seiner 10-jährigen Tätigkeit im Bereich EDV-Konzeption bei der Firma Nordlauf ist er weit reichende Erfahrung im Bereich der IT aufgebaut. Zur Zeit leitet er Projekte mittelständischer Unternehmen zur Migration in die Cloud.</p>
<p class="founder-quote">„Mein Ziel mit Plorvane ist es, den Stellenwert der IT Services in kleinen Unternehmen zu erhöhen.“</p>
<svg class="abs" style="left:556px;top:4080px" width="90" height="18" fill="none" stroke="#9aa3ad" stroke-width="1.3"><circle cx="10" cy="9" r="6"/><circle cx="45" cy="9" r="6"/><circle cx="80" cy="9" r="6"/></svg>
<div class="abs" style="left:587px;top:4124px;width:26px;height:2px;background:var(--gold)"></div>
<svg class="abs" style="left:252px;top:3962px" width="14" height="26"><path d="M12 2L2 13l10 11" stroke="#ccc" stroke-width="1.3" fill="none"/></svg>
<svg class="abs" style="left:932px;top:3962px" width="14" height="26"><path d="M2 2l10 11L2 24" stroke="#ccc" stroke-width="1.3" fill="none"/></svg>

<div class="social" style="left:256px"><div class="ring">P</div><div class="handle">Plorvane</div></div>
<div class="social" style="left:442px"><div class="ring">P</div><div class="handle">PlorvaneDE</div></div>
<div class="social" style="left:628px"><div class="ring">P</div><div class="handle">Plorvaneplug</div></div>
<div class="social" style="left:812px"><div class="ring">P</div><div class="handle">Plorvanede</div></div>

<svg class="abs" style="left:1122px;top:4318px" width="46" height="46"><circle cx="23" cy="23" r="22" fill="#f5b52c"/><rect x="14" y="16" width="18" height="13" rx="2" fill="none" stroke="#fff" stroke-width="1.5"/><path d="M18 29l-2 4 6-4" fill="#fff"/></svg>
<svg class="abs" style="left:1128px;top:4396px" width="34" height="34"><circle cx="17" cy="17" r="15" fill="#fff" stroke="#f5b52c" stroke-width="1.3"/><path d="M17 23V11M12 16l5-5 5 5" stroke="#f5b52c" stroke-width="1.3" fill="none"/></svg>
<div class="abs" style="left:1120px;top:4432px;width:50px;text-align:center;font-size:6px;color:var(--gold)">ON TOP</div>

<footer class="footer">
  <div class="links"><span>DATENSCHUTZ</span><span>|</span><span>AGB</span><span>|</span><span>IMPRESSUM</span></div>
  <div class="copy">© 2019 Plorvane.</div>
</footer>

</body>
</html>
```